Tallow Creek Partners needs an email sign off and professional power point template

Newly formed company and we require:1. graphic email signature on our email , and2.a professional powerpoint template (title page and sub pages) and revamp of the attached powerpoint presentation I have uploaded our business car design (logo and contact details ) and a current powerpoint template we are currently working with. Also a brief of how we operateOur mantra is Discover, Develop, Deliver.

Target Market(s)

multinationals and mid size SME's requiring help to grown new markets or geographies for their business.

Colors
000000

Requirements
Must have
• the mantra..our phases of engagement around assisting clients is:
• 1. Discover
• 2. Develop
• 3. Deliver
Nice to have
• we differentiate ourselves form consultant by actually executing the plan for them (i.e. is the delivery phase)

```html
<!DOCTYPE html>
<html lang="en">
<head>
<meta charset="utf-8">
<title>Tallow Creek Partners – Email Signature &amp; Slide Templates</title>
<link rel="stylesheet" href="https://fonts.googleapis.com/css2?family=Open+Sans:wght@400&family=Roboto:ital,wght@0,400;0,500;0,700;0,900;1,300&display=swap">
<style>
  :root {
    --canvas: #939393;
    --blue: #0a89b9;
    --blue-light: #5cc0e0;
    --blue-pale: #d6ebf3;
    --navy: #10324f;
    --navy-deep: #0d2238;
    --photo-a: #1b6f96;
    --photo-b: #2b93bd;
    --white: #ffffff;
    --ink: #1a1a1a;
    --muted: #8a8a8a;
  }
  * { margin: 0; padding: 0; box-sizing: border-box; }
  html, body { width: 1200px; height: 2711px; overflow: hidden; }
  body { background: var(--canvas); position: relative; font-family: "Roboto", Arial, sans-serif; }

  .sheet-title, .slide-label {
    position: absolute; font-family: "Open Sans", Arial, sans-serif; font-weight: 400;
    color: var(--ink); font-size: 38px; letter-spacing: 0.5px; white-space: nowrap;
  }
  .sheet-title { left: 0; width: 1200px; text-align: center; top: 34px; }

  /* Email signature */
  .signature {
    position: absolute; left: 51px; top: 94px; width: 1099px; height: 258px;
    background: linear-gradient(100deg, #eaf5f9 0%, var(--blue-pale) 60%, #c9e3ee 100%);
    overflow: hidden;
  }
  .signature__swoosh { position: absolute; inset: 0; }
  .signature__brand {
    position: absolute; left: 0; top: 0; width: 181px; height: 258px;
    background: var(--navy-deep); display: flex; align-items: center; justify-content: center;
    text-align: center; padding: 0 14px;
  }
  .brand-name { color: var(--white); font-weight: 700; font-size: 26px; line-height: 1.15; text-transform: uppercase; }
  .contact { position: absolute; top: 36px; color: var(--navy); }
  .contact--first { left: 289px; }
  .contact--second { left: 687px; }
  .contact__name { font-weight: 700; font-size: 32px; line-height: 1.1; }
  .contact__role {
    font-weight: 500; font-size: 19px; color: #2c4d7a; padding-bottom: 6px;
    border-bottom: 3px solid #5a74a8; width: 334px; margin-bottom: 14px;
  }
  .contact__line { font-weight: 500; font-size: 19px; line-height: 1.3; }
  .contact__social { display: flex; gap: 6px; margin-top: 6px; }
  .contact__social span { width: 21px; height: 21px; border-radius: 50%; background: var(--navy); display: block; }

  /* Slides */
  .slide { position: absolute; width: 640px; height: 360px; background: var(--white); overflow: hidden; }
  .slide__chrome { position: absolute; inset: 0; }
  .slide__heading {
    position: absolute; left: 20px; top: 10px; color: var(--white); font-weight: 700;
    font-size: 34px; line-height: 40px; text-transform: uppercase;
  }
  .slide__body { position: absolute; left: 20px; top: 88px; color: var(--muted); font-size: 17px; }
  .slide__footer-text {
    position: absolute; left: 210px; top: 345px; font-size: 10px; color: var(--white);
    line-height: 12px; text-transform: uppercase; white-space: nowrap;
  }

  .slide--cover { background: linear-gradient(135deg, var(--photo-a), var(--photo-b)); }
  .cover__brand {
    position: absolute; left: 12px; top: 22px; width: 228px; height: 316px;
    background: var(--navy-deep); display: flex; align-items: center; justify-content: center;
    text-align: center; padding: 0 18px;
  }
  .cover__brand .brand-name { font-size: 34px; }
  .cover__title {
    position: absolute; left: 262px; top: 98px; color: var(--white); font-weight: 700;
    font-size: 42px; line-height: 1.05; text-align: center; text-transform: uppercase;
  }

  .slide--intro .intro__title {
    position: absolute; left: 0; width: 325px; top: 118px; text-align: center;
    color: var(--blue); font-weight: 900; font-size: 36px; line-height: 1.1;
  }
  .intro__photo {
    position: absolute; left: 325px; top: 0; width: 315px; height: 360px;
    background: linear-gradient(160deg, #4fb0d3, #2a8fb8 70%, #3d9fc6);
  }
  .intro__mantra {
    position: absolute; left: 325px; width: 315px; top: 92px; text-align: center;
    color: var(--white); font-style: italic; font-weight: 300; font-size: 38px; line-height: 60px;
  }

  .flow-box { position: absolute; width: 134px; height: 58px; background: var(--blue); box-shadow: 3px 3px 0 #a9d6e6; }
  .flow-center { position: absolute; left: 213px; top: 145px; width: 217px; height: 92px; background: #5bb8d6; }
</style>
</head>
<body>

<h1 class="sheet-title">EMAIL SIGNATURE</h1>

<section class="signature" aria-label="Email signature">
  <svg class="signature__swoosh" width="1099" height="258" viewBox="0 0 1099 258" aria-hidden="true">
    <path d="M181 258 C 420 170, 760 90, 1099 40 L1099 0 C 760 60, 430 150, 181 230 Z" fill="#ffffff" opacity="0.75"/>
    <path d="M700 0 C 850 30, 980 60, 1099 110 L1099 70 C 980 35, 870 10, 780 0 Z" fill="#ffffff" opacity="0.55"/>
  </svg>
  <div class="signature__brand"><span class="brand-name">Tallow Creek Partners</span></div>
  <div class="contact contact--first">
    <p class="contact__name">Martin Hale</p>
    <p class="contact__role">Principal, Tallow Creek Partners</p>
    <p class="contact__line">0400 118 240</p>
    <p class="contact__line">martin@tallowcreek.com</p>
    <p class="contact__line">www.tallowcreek.com</p>
    <div class="contact__social"><span></span><span></span><span></span></div>
  </div>
  <div class="contact contact--second">
    <p class="contact__name">Owen Pryce</p>
    <p class="contact__role">Principal, Tallow Creek Partners</p>
    <p class="contact__line">0400 372 916</p>
    <p class="contact__line">owen@tallowcreek.com</p>
    <p class="contact__line">www.tallowcreek.com</p>
    <div class="contact__social"><span></span><span></span><span></span></div>
  </div>
</section>

<!-- Slide 1: cover -->
<section class="slide slide--cover" style="left:51px; top:379px;" role="img" aria-label="Cover slide over a blue-toned photo of a business meeting desk">
  <div class="cover__brand"><span class="brand-name">Tallow Creek Partners</span></div>
  <p class="cover__title">Tallow<br>Creek<br>Partners</p>
</section>
<p class="slide-label" style="left:741px; top:520px;">SAMPLE SLIDE #1</p>

<!-- Slide 2: intro -->
<section class="slide slide--intro" style="left:481px; top:761px;">
  <p class="intro__title">Tallow<br>Creek<br>Partners</p>
  <div class="intro__photo" role="img" aria-label="Blue-toned photo of a tablet showing growth charts"></div>
  <p class="intro__mantra">Discover<br>Develop<br>Deliver</p>
</section>
<p class="slide-label" style="left:99px; top:932px;">SAMPLE SLIDE #2</p>

<!-- Slide 3 -->
<section class="slide" style="left:51px; top:1142px;">
  <svg class="slide__chrome" width="640" height="360" viewBox="0 0 640 360" aria-hidden="true">
    <polygon points="0,0 500,0 468,60 0,60" fill="#0a89b9"/>
    <polygon points="510,0 560,0 532,30 482,30" fill="#5cc0e0"/>
    <polygon points="60,344 640,344 640,356 70,356" fill="#0a89b9"/>
    <polygon points="18,330 26,330 46,356 38,356" fill="#0a89b9"/>
    <polygon points="30,334 38,334 56,356 48,356" fill="#5cc0e0"/>
    <polygon points="600,340 608,340 628,360 620,360" fill="#0a89b9"/>
  </svg>
  <h2 class="slide__heading">Discover</h2>
  <p class="slide__body">Insert Details Here</p>
  <p class="slide__footer-text">TCP - Discover, Develop, Deliver</p>
</section>
<p class="slide-label" style="left:744px; top:1317px;">SAMPLE SLIDE #3</p>

<!-- Slide 4 -->
<section class="slide" style="left:481px; top:1523px;">
  <svg class="slide__chrome" width="640" height="360" viewBox="0 0 640 360" aria-hidden="true">
    <polygon points="0,0 500,0 468,60 0,60" fill="#0a89b9"/>
    <polygon points="510,0 560,0 532,30 482,30" fill="#5cc0e0"/>
    <polygon points="60,344 640,344 640,356 70,356" fill="#0a89b9"/>
    <polygon points="18,330 26,330 46,356 38,356" fill="#0a89b9"/>
    <polygon points="30,334 38,334 56,356 48,356" fill="#5cc0e0"/>
    <polygon points="600,340 608,340 628,360 620,360" fill="#0a89b9"/>
  </svg>
  <h2 class="slide__heading">Develop</h2>
  <p class="slide__body">Insert Details Here</p>
  <p class="slide__footer-text">TCP - Discover, Develop, Deliver</p>
</section>
<p class="slide-label" style="left:99px; top:1695px;">SAMPLE SLIDE #4</p>

<!-- Slide 5 -->
<section class="slide" style="left:51px; top:1905px;">
  <svg class="slide__chrome" width="640" height="360" viewBox="0 0 640 360" aria-hidden="true">
    <polygon points="0,0 500,0 468,60 0,60" fill="#0a89b9"/>
    <polygon points="510,0 560,0 532,30 482,30" fill="#5cc0e0"/>
    <polygon points="60,344 640,344 640,356 70,356" fill="#0a89b9"/>
    <polygon points="18,330 26,330 46,356 38,356" fill="#0a89b9"/>
    <polygon points="30,334 38,334 56,356 48,356" fill="#5cc0e0"/>
    <polygon points="600,340 608,340 628,360 620,360" fill="#0a89b9"/>
  </svg>
  <h2 class="slide__heading">Deliver</h2>
  <p class="slide__body">Insert Details Here</p>
  <p class="slide__footer-text">TCP - Discover, Develop, Deliver</p>
</section>
<p class="slide-label" style="left:744px; top:2060px;">SAMPLE SLIDE #5</p>

<!-- Slide 6: process diagram -->
<section class="slide" style="left:481px; top:2286px;">
  <svg class="slide__chrome" width="640" height="360" viewBox="0 0 640 360" aria-hidden="true">
    <polygon points="0,0 500,0 468,60 0,60" fill="#0a89b9"/>
    <polygon points="510,0 560,0 532,30 482,30" fill="#5cc0e0"/>
    <polygon points="60,344 640,344 640,356 70,356" fill="#0a89b9"/>
    <polygon points="18,330 26,330 46,356 38,356" fill="#0a89b9"/>
    <polygon points="30,334 38,334 56,356 48,356" fill="#5cc0e0"/>
    <polygon points="600,340 608,340 628,360 620,360" fill="#0a89b9"/>
    <g stroke="#5cc0e0" stroke-width="3" fill="#5cc0e0">
      <line x1="196" y1="99" x2="212" y2="99"/><polygon points="218,99 210,94 210,104" stroke="none"/>
      <line x1="424" y1="99" x2="440" y2="99"/><polygon points="446,99 438,94 438,104" stroke="none"/>
      <line x1="551" y1="140" x2="551" y2="152"/><polygon points="551,158 546,150 556,150" stroke="none"/>
      <line x1="551" y1="231" x2="551" y2="243"/><polygon points="551,249 546,241 556,241" stroke="none"/>
      <line x1="446" y1="281" x2="430" y2="281"/><polygon points="424,281 432,276 432,286" stroke="none"/>
      <line x1="218" y1="281" x2="202" y2="281"/><polygon points="196,281 204,276 204,286" stroke="none"/>
      <line x1="94" y1="246" x2="94" y2="234"/><polygon points="94,228 89,236 99,236" stroke="none"/>
      <line x1="94" y1="155" x2="94" y2="143"/><polygon points="94,137 89,145 99,145" stroke="none"/>
    </g>
  </svg>
  <h2 class="slide__heading">Insert Headline Here</h2>
  <div class="flow-box" style="left:27px; top:70px;"></div>
  <div class="flow-box" style="left:255px; top:70px;"></div>
  <div class="flow-box" style="left:484px; top:70px;"></div>
  <div class="flow-box" style="left:27px; top:161px;"></div>
  <div class="flow-box" style="left:484px; top:161px;"></div>
  <div class="flow-box" style="left:27px; top:253px;"></div>
  <div class="flow-box" style="left:255px; top:253px;"></div>
  <div class="flow-box" style="left:484px; top:253px;"></div>
  <div class="flow-center"></div>
  <p class="slide__footer-text">TCP - Discover, Develop, Deliver</p>
</section>
<p class="slide-label" style="left:99px; top:2461px;">SAMPLE SLIDE #6</p>

</body>
</html>
```